Certificate of Completion - Educational Trainings

We are looking for a certificate of completion for individuals who complete one of our specific trainings. Files should be provided in a Word (docx) or PowerPoint (pptx) format. The "Talmoray example.png" file is to show necessary information. Copies of logos have been included for design purposes.

Target Market(s)

Training Participants

Industry/Entity Type

Healthcare

Font styles to use
Sans Serif

```html
<!DOCTYPE html>
<html lang="en">
<head>
<meta charset="utf-8">
<title>Talmoray Certificate of Completion</title>
<link rel="stylesheet" href="https://fonts.googleapis.com/css2?family=Montserrat:wght@800&family=Oranienbaum&family=Poppins:wght@400;600;700&family=Prata&display=swap">
<style>
  :root {
    --paper: #fdfcf6;
    --frame: #6ab04c;
    --forest: #0f6b2c;
    --ink: #111111;
    --gold: #e9b649;
    --gold-soft: rgba(247, 205, 120, 0.55);
  }
  * { margin: 0; padding: 0; box-sizing: border-box; }
  html, body { width: 1200px; height: 848px; overflow: hidden; background: var(--paper); }
  .certificate {
    position: relative;
    width: 1200px;
    height: 848px;
    background: var(--paper);
    border: 4px solid var(--frame);
    font-family: "Poppins", sans-serif;
    color: var(--ink);
  }
  .corner-ornament {
    position: absolute;
    width: 220px;
    height: 240px;
  }
  .corner-ornament.top-left { top: 8px; left: 8px; background: radial-gradient(ellipse at 0 0, var(--gold) 0%, var(--gold-soft) 40%, rgba(253,252,246,0) 72%); }
  .corner-ornament.top-right { top: 8px; right: 8px; background: radial-gradient(ellipse at 100% 0, var(--gold) 0%, var(--gold-soft) 40%, rgba(253,252,246,0) 72%); }
  .corner-ornament.bottom-left { bottom: 8px; left: 8px; background: radial-gradient(ellipse at 0 100%, var(--gold) 0%, var(--gold-soft) 40%, rgba(253,252,246,0) 72%); }
  .corner-ornament.bottom-right { bottom: 8px; right: 8px; background: radial-gradient(ellipse at 100% 100%, var(--gold) 0%, var(--gold-soft) 40%, rgba(253,252,246,0) 72%); }

  .centered { position: absolute; left: 0; right: 0; text-align: center; }

  .brand { top: 38px; display: flex; justify-content: center; align-items: center; gap: 16px; }
  .brand-dot { width: 40px; height: 40px; border-radius: 50%; background: var(--forest); }
  .brand-name { font-family: "Montserrat", sans-serif; font-weight: 800; font-size: 38px; letter-spacing: 2px; color: var(--ink); }

  .sponsor-line { top: 97px; font-weight: 700; font-size: 15.5px; letter-spacing: -0.1px; }

  .title { top: 130px; font-family: "Prata", serif; font-size: 104px; line-height: 1; color: var(--forest); letter-spacing: 2px; }
  .subtitle { top: 230px; font-family: "Oranienbaum", serif; font-size: 54px; line-height: 1; letter-spacing: 3px; }
  .awarded { top: 298px; font-size: 22px; letter-spacing: 3.6px; }

  .name-line { position: absolute; top: 411px; left: 275px; width: 676px; height: 2px; background: var(--frame); }

  .course-details { top: 425px; font-size: 19px; letter-spacing: 2.6px; line-height: 27.7px; }
  .course-details .field { font-weight: 700; }

  .signature { position: absolute; top: 674px; text-align: center; }
  .signature .rule { height: 1px; background: var(--frame); }
  .signature .label { margin-top: 12px; font-weight: 700; font-size: 19.5px; letter-spacing: 0.8px; }
  .signature.date { left: 264px; width: 208px; }
  .signature.consultant { left: 725px; width: 226px; }

  .seal { position: absolute; top: 636px; left: 540px; width: 132px; text-align: center; }
  .seal-dot { width: 64px; height: 64px; margin: 0 auto 8px; border-radius: 50%; background: var(--forest); }
  .seal-name { font-family: "Montserrat", sans-serif; font-weight: 800; font-size: 18px; letter-spacing: 1px; color: var(--ink); }

  .accreditation { top: 775px; font-size: 16.2px; line-height: 24px; }
</style>
</head>
<body>
  <main class="certificate">
    <div class="corner-ornament top-left" role="img" aria-label="Gold floral corner ornament"></div>
    <div class="corner-ornament top-right" role="img" aria-label="Gold floral corner ornament"></div>
    <div class="corner-ornament bottom-left" role="img" aria-label="Gold floral corner ornament"></div>
    <div class="corner-ornament bottom-right" role="img" aria-label="Gold floral corner ornament"></div>

    <header class="centered brand">
      <span class="brand-dot"></span>
      <span class="brand-name">TALMORAY</span>
    </header>
    <p class="centered sponsor-line">48 HARBOR LANE, STE. 310, BROOKVALE, ME 04871 | NATIONAL BOARD SPONSOR NUMBER 58203</p>

    <h1 class="centered title">CERTIFICATE</h1>
    <h2 class="centered subtitle">OF COMPLETION</h2>
    <p class="centered awarded">THIS CERTIFICATE IS AWARDED TO</p>

    <div class="name-line"></div>

    <div class="centered course-details">
      <p>FOR SUCCESSFUL COMPLETION OF</p>
      <p>BEST PRACTICES: BUDGET PROCESS / BUDGET BUILDING</p>
      <p>COMPLETED ONLINE</p>
      <p class="field">FIELD OF STUDY FINANCE</p>
      <p>CPE CREDITS : 1</p>
    </div>

    <div class="signature date">
      <div class="rule"></div>
      <p class="label">COMPLETION DATE</p>
    </div>

    <div class="seal">
      <div class="seal-dot"></div>
      <p class="seal-name">TALMORAY</p>
    </div>

    <div class="signature consultant">
      <div class="rule"></div>
      <p class="label">SENIOR CONSULTANT</p>
    </div>

    <p class="centered accreditation">IN ACCORDANCE WITH THE STANDARD OF THE NATIONAL BOARD OF CPE PROVIDERS,<br>CPE CREDITS HAVE BEEN GRANTED BASED ON A 50 MINUTE HOUR.</p>
  </main>
</body>
</html>
```